WEB SITE BRIEF – “STILL MEADOW ENERGY HEALING”
Registration
• The business has been registered as: “Still Meadow Energy Healing.”
• The web site has been registered as: www.stillmeadow.com.au

About Still Meadow Energy Healing
This is a small company that will be performing fully clothed treatments / healings for clients who may have injuries; sickness; stress in life; looking to relax; enegy balance and spiritual help.

Look and Feel

• Green pallet – that aligns to the logo design;
• Consistent design/look and feel throughout the website – ie. Images that come from the same “family”;
• Images – each page needs to have more interest than simply text – we envisage ”Reiki” related images on each page – See “Images” below.
• Premium – the design needs to be clean and information easily readable
• Simple and clear navigation

Functionality
Note we need to be able to edit and update the finished web site - Coding Required
• Simple content management system that we can easily update ourselves after website is complete
• Need the website address to match the url

Design References:
Looking for a nice simple to navigate website.
Below are some references to existing web sites that we quite like:

http://www.marthavale.com.au/construction/
This one looks and feels professional

http://www.brookfieldgardens.com.au/
This one feels very clean

http://www.tallpinesyards.com.au/products
This one as it looks clean and smart
 

Examples of Images for each page:
Please note that I do not want to use any photos of people receiving treatments who are not wearing clothes or who are wearing towels, as this is not the service i am providing. All my treatments will be fully clothed so I do not want to give the impression that they will have to remove any clothing. Thank you

Examples of “Reiki” related images that we quite like are:
• http://www.pictarvault.com/stock-illustration-40918276-chakra-and-meditation.php?st=5190642
• http://www.pictarvault.com/stock-illustration-6127403-healing-hands.php?st=5190642

SEO – organic search only
• We require advise as to how best optimise the website for organic search
o Linking to other websites
o Zentara +
o Zentara map of location?
o Update of content frequently?

Review
We would like to have the ability to review a draft of the web site design prior to finalisation.

WEB SITE CONTENT

- Please see attached file 'Detailed Layout Of Website and Content.
- Please include logo on home page.
- Please follow home page menu options as shown
- Please include all text and images provided
Updates

hi thanks for all your designs so far, i just want to make it clear that i don't want to use any photos where the client is having a treatment with no clothes on. This is not the treatments i will be giving so i don't want to give the wrong impression. As it states in the brief i want to use my logo provided (tree) and image/s of nature for the homepage and have a clear navigation menu to the different sections. Please include my picture in the about section; also include the picture of the healing room provided, as well as other images similar to the examples provided. 

Thank you

Target Market(s)

People who are looking for 'alternative' healing methods.
People interested in reiki for relaxation purposes.
People who have tried conventional medicines and have not been able to be cured/healed.
People of all ages.

Industry/Entity Type

Business

Requirements
Must have
• Please see 'design breif" and 'web content" above.
Codding required - Must be able to easily edit and modify and update after site is complete.
Nice to have
• Pictures of nature example waterfall on home page
Should not have
• Pictures of people receiving treatments with no clothes or wearing towels. As all treatments will be fully clothed and i don't want to give the idea that you must remove any clothing.

```html
<!DOCTYPE html>
<html lang="en">
<head>
<meta charset="utf-8">
<title>Still Meadow Energy Healing</title>
<link href="https://fonts.googleapis.com/css2?family=Ubuntu:ital,wght@0,400;0,500;1,400;1,500&family=Cinzel:wght@400&family=Cormorant+Garamond:wght@500&display=swap" rel="stylesheet">
<style>
:root{
  --green:#6a931f;
  --green-dark:#4f7a1a;
  --nav:#5f9a3a;
  --nav-line:#4c8229;
  --text:#333;
  --heading:#3d3d3d;
  --red:#c8191c;
  --logo-green:#2f5a22;
  --card:#fff;
}
*{margin:0;padding:0;box-sizing:border-box}
html,body{width:1029px;height:1200px;overflow:hidden}
body{position:relative;background:var(--green);font-family:"Ubuntu",sans-serif;color:var(--text)}
.abs{position:absolute}

.header-scene{left:0;top:0;width:1029px;height:211px;
  background:
    linear-gradient(180deg,rgba(255,255,255,.55),rgba(255,255,255,.75)),
    linear-gradient(90deg,#b9c4ad 0%,#e9ece6 14%,#f3f4f1 30%,#dfe4da 52%,#f1f2ee 58%,#e6eadf 72%,#cdd6c2 100%)}
.nature-band{left:0;top:211px;width:1029px;height:415px;
  background:
    linear-gradient(180deg,rgba(0,0,0,0) 70%,rgba(230,235,232,.55) 100%),
    linear-gradient(90deg,#3e4d26 0%,#566b31 2%,#7b8b58 3.5%,#eef2f1 5.5%,#cfd6d2 7%,#8b957a 8.5%,#4d5c33 10.8%,#4d5c33 89%,#8c9a62 91%,#a9ad9f 94%,#6f7466 96.5%,#b7bbb5 98.5%,#8c907f 100%)}

.brand-mark{left:128px;top:12px;width:96px;height:96px;border-radius:50%;background:radial-gradient(circle at 45% 40%,#4e8a2f,#2f5a22)}
.brand-sub{left:118px;top:114px;width:116px;text-align:center;font-family:"Cinzel",serif;color:var(--logo-green);font-size:11.5px;line-height:11px}
.brand-name{left:248px;top:62px;font-family:"Cinzel",serif;color:var(--logo-green);line-height:1}
.brand-name .line1{font-size:26px;display:block}
.brand-name .line2{font-size:17.5px;display:block;margin:5px 0 0 20px}

.follow{left:728px;top:23px;font-size:12.5px;font-weight:500;color:var(--green-dark)}
.social{left:823px;top:16px;display:flex;gap:9px}
.social span{width:26px;height:26px;border-radius:5px;box-shadow:inset 0 -3px 5px rgba(0,0,0,.18)}
.social span:nth-child(1){background:#4f7a3a}
.social span:nth-child(2){background:#7aa64c}
.social span:nth-child(3){background:#a3432f}

.call{left:723px;top:65px;width:195px;height:56px;background:#fff;border-radius:26px;border:1px solid #ddd;box-shadow:inset 0 3px 4px rgba(0,0,0,.12);text-align:center;font-family:"Cormorant Garamond",serif}
.call .label{color:var(--red);font-size:15px;margin-top:3px;display:block}
.call .number{color:var(--logo-green);font-size:35px;line-height:1;display:block;margin-top:-2px}

.nav{left:111px;top:147px;width:806px;height:41px;background:linear-gradient(#67a33f,#5a9236);border-radius:21px;display:flex;list-style:none}
.nav li{display:flex;align-items:center;justify-content:center;color:#fff;font-weight:500;font-size:13.5px;letter-spacing:.3px;border-left:1px solid var(--nav-line)}
.nav li:first-child{border-left:none}

.slider{left:111px;top:198px;width:807px;height:409px;background:#fff;box-shadow:0 1px 4px rgba(0,0,0,.3)}
.slide-art{left:5px;top:5px;width:797px;height:399px;
  background:
    radial-gradient(ellipse 38% 55% at 50% 38%,rgba(120,220,250,.95) 0%,rgba(60,150,230,.6) 40%,rgba(40,80,190,0) 75%),
    linear-gradient(90deg,#2a1f7e 0%,#2b3fa6 25%,#2c62c4 50%,#2b3fa6 75%,#2a1f7e 100%)}
.arrow{top:186px}

.card{left:111px;top:617px;width:807px;height:508px;background:var(--card);border-radius:10px}
.kicker{color:var(--green);font-weight:500;font-size:23px;line-height:1}
.h-big{color:var(--heading);font-weight:500;font-size:22.5px;line-height:1;margin-top:2px;letter-spacing:.4px}
.welcome{left:135px;top:640px;width:472px}
.tagline{margin-top:10px;color:var(--green);font-style:italic;font-weight:500;font-size:13px;line-height:21px}
.intro{margin-top:9px;font-size:11.7px;line-height:19.7px}
.rule{height:1px;background:#ddd}
.testimonials{left:135px;top:876px}
.avatar{width:64px;height:58px;border:1px solid #ddd;background:#fff;padding:3px;box-shadow:0 1px 2px rgba(0,0,0,.12)}
.avatar div{width:100%;height:100%;background:linear-gradient(#f1f1f1,#d9d9d9)}
.quote{width:396px;height:58px;border-radius:5px;background:linear-gradient(#fff,#efefef);box-shadow:0 1px 4px rgba(0,0,0,.18);padding:9px 44px 0 14px;font-size:10.3px;font-style:italic;line-height:17px;color:#555}
.quote em{color:var(--green);font-style:italic}
.link{font-size:11px;font-weight:500;color:var(--red);letter-spacing:.3px}
.divider{left:640px;top:652px;width:1px;height:463px;background:#ddd}
.treat-art{left:668px;top:693px;width:225px;height:133px;border:1px solid #ddd;
  background:
    radial-gradient(ellipse 45% 55% at 45% 45%,#fff 0%,#fdf7a0 40%,rgba(250,240,140,0) 75%),
    linear-gradient(135deg,#f4f6e8,#eef2d8 60%,#dfe9e6)}
.treat-list{left:670px;top:831px;list-style:none;font-size:11.5px}
.treat-list li{height:28px;display:flex;align-items:center;gap:11px}
.leaf{width:10px;height:12px}
.contact-block{left:668px;top:1026px;font-size:11.3px;line-height:17.5px}
.contact-block .org{color:var(--green);font-weight:500;font-size:13.5px;margin-bottom:5px}
.contact-block .red{color:var(--red)}
.contact-block .green{color:var(--green)}
.footer{left:0;top:1145px;width:1092px;text-align:center;color:#fff;font-size:11px;line-height:17px}
</style>
</head>
<body>
<div class="abs header-scene" role="img" aria-label="Soft misty forest waterfall backdrop"></div>
<div class="abs nature-band" role="img" aria-label="Waterfall and mossy rocky stream scenery"></div>

<header>
  <div class="abs brand-mark"></div>
  <div class="abs brand-sub">STILL MEADOW<br>ENERGY HEALING</div>
  <div class="abs brand-name"><span class="line1">STILL MEADOW</span><span class="line2">ENERGY HEALING</span></div>
  <div class="abs follow">Follow Us On:</div>
  <div class="abs social"><span></span><span></span><span></span></div>
  <div class="abs call"><span class="label">Call Us Today:</span><span class="number">80457129</span></div>
  <ul class="abs nav">
    <li style="width:118px">HOME</li>
    <li style="width:166px">TREATMENTS</li>
    <li style="width:141px">ABOUT US</li>
    <li style="width:99px">FAQ</li>
    <li style="width:162px">TESTIMONIALS</li>
    <li style="width:120px">CONTACT</li>
  </ul>
</header>

<section class="abs slider">
  <div class="abs slide-art" role="img" aria-label="Chakra meditation illustration with radiating blue light"></div>
  <svg class="abs arrow" style="left:14px" width="26" height="40" viewBox="0 0 26 40"><path d="M20 4 6 20l14 16" fill="none" stroke="#fff" stroke-width="5" stroke-linecap="round" stroke-linejoin="round"/></svg>
  <svg class="abs arrow" style="left:767px" width="26" height="40" viewBox="0 0 26 40"><path d="M6 4l14 16L6 36" fill="none" stroke="#fff" stroke-width="5" stroke-linecap="round" stroke-linejoin="round"/></svg>
</section>

<main class="abs card"></main>

<section class="abs welcome">
  <div class="kicker">Welcome to</div>
  <h1 class="h-big">STILL MEADOW ENERGY HEALING</h1>
  <p class="tagline">Myaim is to provide a healing service to all seeking a positive change and direction to their lives.</p>
  <p class="intro">People often find themselves stuck in seeminglyhopeless situations with no solution in sight. Having been in this situation myself, I discovered the power of energy healing and am committed to helping others achieve the same healing and positive outlook on life. Energy healing can address all issues from simple physical injuries and mental concerns to more profoundproblems where conventional methods have not worked.</p>
</section>
<div class="abs rule" style="left:135px;top:860px;width:470px"></div>

<section class="abs testimonials">
  <div class="kicker">Our</div>
  <h2 class="h-big">TESTIMONIALS</h2>
</section>
<div class="abs avatar" style="left:135px;top:932px"><div role="img" aria-label="Client portrait placeholder"></div></div>
<div class="abs quote" style="left:219px;top:932px">Donec erat purus, faucibus vitae congue vel, porttitor nec lectus vehicula tempus ac sed massa. <em>By Clara Denholm</em></div>
<div class="abs avatar" style="left:135px;top:1009px"><div role="img" aria-label="Client portrait placeholder"></div></div>
<div class="abs quote" style="left:219px;top:1009px">Donec erat purus, faucibus vitae congue vel, porttitor nec lectus vehicula tempus ac sed massa. <em>By Clara Denholm</em></div>
<div class="abs link" style="left:137px;top:1094px">READ ALL TESTIMONIALS</div>

<div class="abs divider"></div>

<section class="abs" style="left:665px;top:640px">
  <div class="kicker">Our</div>
  <h2 class="h-big">TREATMENTS</h2>
</section>
<div class="abs treat-art" role="img" aria-label="Healing hands illustration with radiating yellow light"></div>
<ul class="abs treat-list">
  <li><svg class="leaf" viewBox="0 0 10 12"><path d="M5 1C9 3 9 8 5 11 1 8 1 3 5 1Z" fill="#6a931f"/></svg>Reike</li>
  <li><svg class="leaf" viewBox="0 0 10 12"><path d="M5 1C9 3 9 8 5 11 1 8 1 3 5 1Z" fill="#6a931f"/></svg>Serenity Vibration</li>
  <li><svg class="leaf" viewBox="0 0 10 12"><path d="M5 1C9 3 9 8 5 11 1 8 1 3 5 1Z" fill="#6a931f"/></svg>Combined Reike/ Serenity</li>
</ul>
<div class="abs link" style="left:668px;top:928px">READ MORE</div>
<div class="abs rule" style="left:665px;top:962px;width:228px"></div>

<section class="abs" style="left:665px;top:976px">
  <div class="kicker">Our</div>
  <h2 class="h-big">CONTACT</h2>
</section>
<address class="abs contact-block" style="font-style:normal">
  <div class="org">Still Meadow Energy Healing</div>
  14 Wattle Grove Rd,<br>
  Hollyvale 2081<br>
  <span class="red">Tel:</span> 02 80457129<br>
  <span class="red">Email:</span> <span class="green">info@stillmeadow.com.au</span>
</address>

<footer class="abs footer">Copyright © 2013. www.stillmeadow.com.au. All Right Reserved.<br>Privacy Policy</footer>
</body>
</html>
```